Business Card

I need a business card that really pops for a potential customer or person who refers a personal injury lead. I want to highlight our office locations, but only address that needs to be on the card is my office's main address. I want a sleek, modern and minimalist design.

```html
<!DOCTYPE html>
<html lang="en">
<head>
<meta charset="UTF-8">
<title>Lakeshore Injury Counsel – Business Card</title>
<link href="https://fonts.googleapis.com/css2?family=Montserrat:wght@300;400;500;700&display=swap" rel="stylesheet">
<style>
  :root {
    --backdrop: #3b3b3d;
    --card: #262627;
    --card-edge: #2e2e30;
    --wordmark: #b9b9bb;
    --text: #ffffff;
    --rule: #8a8a8c;
  }
  * { box-sizing: border-box; margin: 0; padding: 0; }
  html, body {
    width: 1200px; height: 1200px; overflow: hidden;
    background: var(--backdrop);
    font-family: "Montserrat", Arial, sans-serif;
  }
  .sheet {
    width: 1200px; height: 1200px;
    display: flex; flex-direction: column; align-items: center; justify-content: center;
    gap: 60px;
  }
  .card {
    position: relative;
    width: 900px; height: 514px;
    background: linear-gradient(160deg, var(--card-edge), var(--card));
    border-radius: 40px;
    box-shadow: 0 18px 40px rgba(0,0,0,0.45);
    overflow: hidden;
  }
  .wordmark {
    position: absolute;
    color: var(--wordmark);
    font-weight: 300;
    text-transform: uppercase;
    line-height: 1;
  }
  .wordmark .line-main { display: block; letter-spacing: 0.08em; }
  .wordmark .line-sub { display: block; letter-spacing: 0.55em; }

  /* contact side */
  .card--details .wordmark { left: 180px; top: 96px; }
  .card--details .wordmark .line-main { font-size: 76px; }
  .card--details .wordmark .line-sub { font-size: 24px; margin-top: 14px; }

  .person { position: absolute; left: 90px; bottom: 90px; color: var(--text); }
  .person-name { font-size: 40px; font-weight: 700; letter-spacing: -0.01em; line-height: 1; }
  .person-role { font-size: 24px; font-weight: 400; margin-top: 4px; line-height: 1; }

  .divider {
    position: absolute; left: 470px; top: 300px;
    width: 1px; height: 140px; background: var(--rule);
  }
  .contact-list {
    position: absolute; left: 500px; top: 268px;
    list-style: none; color: var(--text);
    font-size: 19px; font-weight: 400; line-height: 1.3;
  }
  .contact-list li { display: flex; align-items: flex-start; gap: 10px; margin-bottom: 4px; }
  .contact-list svg { width: 20px; height: 20px; flex: none; margin-top: 2px; fill: var(--text); }

  /* logo side */
  .card--brand .wordmark { left: 0; right: 0; top: 180px; text-align: center; }
  .card--brand .wordmark .line-main { font-size: 104px; }
  .card--brand .wordmark .line-sub { font-size: 30px; margin-top: 20px; padding-left: 0.55em; }
</style>
</head>
<body>
<main class="sheet">
  <section class="card card--details">
    <div class="wordmark">
      <span class="line-main">Lakeshore</span>
      <span class="line-sub">Injury Counsel</span>
    </div>

    <div class="person">
      <p class="person-name">FULL NAME</p>
      <p class="person-role">POSITION</p>
    </div>

    <div class="divider"></div>

    <ul class="contact-list">
      <li>
        <svg viewBox="0 0 24 24" aria-hidden="true"><path d="M6.6 10.8a15.1 15.1 0 0 0 6.6 6.6l2.2-2.2a1 1 0 0 1 1-.25 11.4 11.4 0 0 0 3.6.6 1 1 0 0 1 1 1V20a1 1 0 0 1-1 1A17 17 0 0 1 3 4a1 1 0 0 1 1-1h3.5a1 1 0 0 1 1 1c0 1.25.2 2.45.6 3.6a1 1 0 0 1-.25 1z"/></svg>
        <span>312-555-0148</span>
      </li>
      <li>
        <svg viewBox="0 0 24 24" aria-hidden="true"><path d="M2 5h20v14H2zm2 2v.5l8 5 8-5V7zm0 2.8V17h16V9.8l-8 5z"/></svg>
        <span>info@lakeshorecounsel.com</span>
      </li>
      <li>
        <svg viewBox="0 0 24 24" aria-hidden="true"><path d="M12 2a10 10 0 1 0 0 20 10 10 0 0 0 0-20zm6.9 6h-2.9a15.6 15.6 0 0 0-1.4-3.6A8 8 0 0 1 18.9 8zM12 4c.8 1.2 1.5 2.5 1.9 4h-3.8c.4-1.5 1.1-2.8 1.9-4zM4.3 14a8 8 0 0 1 0-4h3.4a16.5 16.5 0 0 0 0 4zm.8 2H8c.3 1.3.8 2.5 1.4 3.6A8 8 0 0 1 5.1 16zM8 8H5.1a8 8 0 0 1 4.3-3.6C8.8 5.5 8.3 6.7 8 8zm4 12c-.8-1.2-1.5-2.5-1.9-4h3.8c-.4 1.5-1.1 2.8-1.9 4zm2.3-6H9.7a14.7 14.7 0 0 1 0-4h4.6a14.7 14.7 0 0 1 0 4zm.3 5.6c.6-1.1 1.1-2.3 1.4-3.6h2.9a8 8 0 0 1-4.3 3.6zm1.7-5.6a16.5 16.5 0 0 0 0-4h3.4a8 8 0 0 1 0 4z"/></svg>
        <span>lakeshorecounsel.com</span>
      </li>
      <li>
        <svg viewBox="0 0 24 24" aria-hidden="true"><path d="M12 2a7 7 0 0 0-7 7c0 5.2 7 13 7 13s7-7.8 7-13a7 7 0 0 0-7-7zm0 9.5A2.5 2.5 0 1 1 12 6.5a2.5 2.5 0 0 1 0 5z"/></svg>
        <span>480 West Harbor Avenue,<br>Suite 1200 - Chicago, IL 60601</span>
      </li>
    </ul>
  </section>

  <section class="card card--brand">
    <div class="wordmark">
      <span class="line-main">Lakeshore</span>
      <span class="line-sub">Injury Counsel</span>
    </div>
  </section>
</main>
</body>
</html>
```